Design for "Vellow" protein health bars wrappers

I need a new design for a protein bar that my partners and I are launching for the North American and European markets.
The bar's name is "Vellow."
Given the masculine/aggressive nature of that name, we are thinking of neutralizing it with a more feminine/soft font and design. But hey - the sky is the limit. We obviously want this 20-gram protein bar to sell to a wide net (not just men but women also). So if it means having a Pellam Comic font/design (or whatever) in order to do this, so be it. I leave it up to your intelligence and experience.

ADDED ON FEBRUARY 24:

The official name of the bar is just "VELLOW" (not "Vellow Protein").

We have six flavors divided into two categories, which are 1) SOFT and 2) CRUNCHY.
So, the idea is to make two similar designs for the wrapper that still distinguish themselves from each other because one is 'soft' and the other is 'crunchy.'
Then, within each category, the idea is to have three color variations, designating the three flavors in each category.

Please look at the dimensions and examples of the generic wrapper designs that we already have (and which we find too generic), which I have uploaded.

Target Market(s)

North America - Brindle, Fair Harvest
Europe - Norway, Sweden, Denmark, Germany, France, Switzerland, Italy.

Industry/Entity Type

Nutrition

Logo Text

Vellow

Font styles to use
Serif
Decorative

Colors
fff6dc
f04a50

Requirements
Must have
• The title is "Vellow".
• We have six flavors divided into two categories, which are 1) SOFT and 2) CRUNCHY.
• You can work on the two different types of similar-but-different designs for the "soft" and for the "cruncy." Then it's just a question of color variations for each flavor.
• The flavors are:
• SOFT: 1) strawberry, 2) Chocolate brownie, 3) Cinnamon Crunch
• CRUNCY: 1) Peanut, 2) Lemon, 3) Coconut.
• On the side or at the bottom, there should be stated:
• "20 gm protein"
• "children friendly"
Nice to have
• Obvious: a design that catches the eye and inspires someone to buy the bar to eat it.
• Part of the design could include a photograph of the actual bar (you can use generic photos for that until we place a pic of the actual bar). Like 1/4th of the total surface (or even a little smaller).

```html
<!DOCTYPE html>
<html lang="en">
<head>
<meta charset="utf-8">
<title>VELLOW Protein Bar Wrappers</title>
<link rel="stylesheet" href="https://fonts.googleapis.com/css2?family=Russo+One&family=Cabin:wght@700&family=Pinyon+Script&display=swap">
<style>
  :root{
    --stage:#f1f1f1;
    --peach:#fde4d6;
    --berry-blue:#1d5894;
    --berry-green:#4f9a3c;
    --ink-blue:#21558f;
    --night:#0d0d0d;
    --crimson:#e3262d;
    --white:#ffffff;
    --silver:#e4e6ea;
    --pill-edge:#9aa1aa;
    --bar-light:#e1b97a;
    --bar-dark:#b5833f;
    --berry-red:#d8242d;
    --coco-brown:#7a4a2b;
  }
  *{margin:0;padding:0;box-sizing:border-box}
  html,body{width:1200px;height:801px;overflow:hidden}
  body{background:var(--stage);position:relative;font-family:"Cabin",sans-serif}

  .wrapper{position:absolute}
  .wrapper svg.wrapper-art{position:absolute;inset:0;display:block}
  .wrapper--strawberry{left:104px;top:145px;width:732px;height:260px}
  .wrapper--coconut{left:380px;top:410px;width:736px;height:270px}

  .brand-name{position:absolute;font-family:"Russo One",sans-serif;font-weight:400;letter-spacing:6px;line-height:1}
  .wrapper--strawberry .brand-name{left:62px;top:40px;font-size:82px;color:var(--ink-blue)}
  .wrapper--coconut .brand-name{left:66px;top:48px;font-size:82px;color:var(--silver)}

  .product-pill{position:absolute;height:42px;border-radius:21px;background:var(--white);border:3px solid var(--pill-edge);
    display:flex;align-items:center;justify-content:center;font-family:"Cabin",sans-serif;font-weight:700;font-size:29px;letter-spacing:.5px}
  .wrapper--strawberry .product-pill{left:280px;top:122px;width:265px;color:var(--ink-blue)}
  .wrapper--coconut .product-pill{left:260px;top:124px;width:266px;color:var(--crimson)}

  .flavour-name{position:absolute;font-family:"Pinyon Script",cursive;color:var(--white);line-height:1}
  .wrapper--strawberry .flavour-name{left:214px;top:162px;font-size:50px}
  .wrapper--coconut .flavour-name{left:260px;top:168px;font-size:48px}

  .protein-claim{position:absolute;font-family:"Cabin",sans-serif;font-weight:700;font-size:26px;line-height:1}
  .wrapper--strawberry .protein-claim{left:262px;top:210px;color:var(--white)}
  .wrapper--coconut .protein-claim{left:246px;top:212px;color:var(--night)}

  .kids-badge{position:absolute;width:72px;height:72px;border-radius:50%}
  .wrapper--strawberry .kids-badge{left:125px;top:148px;background:var(--berry-blue);border:4px solid var(--white)}
  .wrapper--coconut .kids-badge{left:108px;top:152px;background:var(--crimson);border:4px solid var(--white)}
</style>
</head>
<body>

<section class="wrapper wrapper--strawberry" aria-label="VELLOW strawberry protein bar wrapper">
  <svg class="wrapper-art" width="732" height="260" viewBox="0 0 732 260">
    <defs>
      <pattern id="crimp-peach" width="10" height="16" patternUnits="userSpaceOnUse">
        <polygon points="10,0 0,8 10,16" fill="#fde4d6"/>
      </pattern>
      <pattern id="crimp-tan" width="10" height="16" patternUnits="userSpaceOnUse">
        <polygon points="0,0 10,8 0,16" fill="#c99a55"/>
      </pattern>
      <linearGradient id="bar-tone-a" x1="0" y1="0" x2="1" y2="1">
        <stop offset="0" stop-color="#e6c287"/>
        <stop offset="1" stop-color="#b5833f"/>
      </linearGradient>
      <radialGradient id="berry-tone" cx=".4" cy=".4" r=".7">
        <stop offset="0" stop-color="#f0444a"/>
        <stop offset="1" stop-color="#a8161d"/>
      </radialGradient>
    </defs>
    <rect x="0" y="0" width="10" height="260" fill="url(#crimp-peach)"/>
    <rect x="722" y="0" width="10" height="260" fill="url(#crimp-tan)"/>
    <rect x="10" y="0" width="712" height="260" fill="var(--peach)"/>
    <polygon points="10,246 722,8 722,18 10,256" fill="var(--berry-green)"/>
    <polygon points="10,254 722,16 722,260 10,260" fill="var(--berry-blue)"/>
    <g role="img" aria-label="Photo of the protein bar">
      <polygon points="566,78 700,40 722,40 722,252 600,252 566,200" fill="url(#bar-tone-a)"/>
    </g>
    <g role="img" aria-label="Photo of a fresh strawberry">
      <ellipse cx="540" cy="196" rx="46" ry="44" fill="url(#berry-tone)"/>
    </g>
    <g stroke="#ffffff" stroke-opacity=".45" stroke-width="2">
      <line x1="22" y1="6" x2="22" y2="254"/><line x1="30" y1="6" x2="30" y2="254"/><line x1="38" y1="6" x2="38" y2="254"/>
      <line x1="694" y1="6" x2="694" y2="254"/><line x1="702" y1="6" x2="702" y2="254"/><line x1="710" y1="6" x2="710" y2="254"/>
    </g>
  </svg>
  <div class="brand-name">VELLOW</div>
  <div class="product-pill">PROTEIN BAR</div>
  <div class="kids-badge" aria-label="Children friendly badge"></div>
  <div class="flavour-name">Strawberry</div>
  <div class="protein-claim">20 gm protein</div>
</section>

<section class="wrapper wrapper--coconut" aria-label="VELLOW coconut protein bar wrapper">
  <svg class="wrapper-art" width="736" height="270" viewBox="0 0 736 270">
    <defs>
      <pattern id="crimp-night" width="10" height="16" patternUnits="userSpaceOnUse">
        <polygon points="10,0 0,8 10,16" fill="#0d0d0d"/>
      </pattern>
      <pattern id="crimp-tan-2" width="10" height="16" patternUnits="userSpaceOnUse">
        <polygon points="0,0 10,8 0,16" fill="#c99a55"/>
      </pattern>
      <linearGradient id="bar-tone-b" x1="0" y1="0" x2="1" y2="1">
        <stop offset="0" stop-color="#e6c287"/>
        <stop offset="1" stop-color="#b5833f"/>
      </linearGradient>
      <radialGradient id="coco-tone" cx=".6" cy=".5" r=".7">
        <stop offset="0" stop-color="#f4efe6"/>
        <stop offset=".45" stop-color="#a36a42"/>
        <stop offset="1" stop-color="#5e3720"/>
      </radialGradient>
    </defs>
    <rect x="0" y="0" width="10" height="270" fill="url(#crimp-night)"/>
    <rect x="726" y="0" width="10" height="270" fill="url(#crimp-tan-2)"/>
    <rect x="10" y="0" width="716" height="270" fill="var(--night)"/>
    <polygon points="480,60 726,2 726,10 500,62" fill="var(--white)"/>
    <polygon points="10,262 726,22 726,34 10,270" fill="var(--white)"/>
    <polygon points="10,270 726,34 726,270" fill="var(--crimson)"/>
    <polygon points="560,82 726,50 726,270 700,270 600,240 545,160" fill="var(--night)" opacity=".25"/>
    <g role="img" aria-label="Photo of the protein bar">
      <polygon points="536,100 690,56 726,56 726,240 620,240 540,200" fill="url(#bar-tone-b)"/>
    </g>
    <g role="img" aria-label="Photo of a whole and a halved coconut">
      <ellipse cx="530" cy="194" rx="68" ry="50" fill="url(#coco-tone)"/>
    </g>
    <g stroke="#ffffff" stroke-opacity=".3" stroke-width="2">
      <line x1="22" y1="6" x2="22" y2="264"/><line x1="30" y1="6" x2="30" y2="264"/>
      <line x1="706" y1="6" x2="706" y2="264"/><line x1="714" y1="6" x2="714" y2="264"/>
    </g>
  </svg>
  <div class="brand-name">VELLOW</div>
  <div class="product-pill">PROTEIN BAR</div>
  <div class="kids-badge" aria-label="Children friendly badge"></div>
  <div class="flavour-name">Coconut</div>
  <div class="protein-claim">20 gm protein</div>
</section>

</body>
</html>
```